Contemporary Elegant Business Card Design for an International Trade Company in the Wine Industry

We need a new business card design for an international trade company in the wine and winemaking industry. The overall feel of the card should be contemporary, upscale, luxurious and elegant. It should communicate confidence and professionalism. The colors should complementary to our logo design (burgundy, gold, and black).
Inspiration: rich velvet tapestry
The card should include the following information:
Business: Brovenna Trading/Shipping, LLC.
Name: Marcus T. Hollenbrand
Title: CEO
Email: mark@brovennatrading.example
Phone: 555-294-6172
www.brovennatrading.example
Updates
Project Deadline Extended
Reason: We'd like the designers that we requested some additional designs from to still submit designs. Thank you!
Industry/Entity Type
Business
Contact Information for Business Card
Title: CEO
Phone: 555-294-6172
www.brovennatrading.example
Look and feel

```html
<!DOCTYPE html>
<html lang="en">
<head>
<meta charset="utf-8">
<title>Brovenna Trading / Shipping — Business Card</title>
<link href="https://fonts.googleapis.com/css2?family=Open+Sans:wght@400;600;700&display=swap" rel="stylesheet">
<style>
  :root {
    --burgundy: #6b111b;
    --burgundy-deep: #5c0d16;
    --gold: #d29a2e;
    --ink: #111111;
    --paper: #ffffff;
    --backdrop: #e9e6e2;
  }
  * { box-sizing: border-box; margin: 0; padding: 0; }
  html, body { width: 1200px; height: 1000px; overflow: hidden; }
  body {
    position: relative;
    background: var(--backdrop);
    font-family: "Open Sans", Arial, sans-serif;
  }
  .card {
    position: absolute;
    left: 265px;
    width: 665px;
    height: 396px;
    box-shadow: 0 4px 14px rgba(0,0,0,0.25);
    overflow: hidden;
  }
  .card--front { top: 73px; background: var(--paper); }
  .card--back { top: 532px; background: var(--burgundy); }

  .brand { position: absolute; left: 35px; top: 34px; width: 160px; text-align: center; }
  .brand__mark {
    display: block; width: 120px; height: 120px; margin: 0 auto 40px;
    background: var(--burgundy);
  }
  .brand__name {
    font-size: 30px; font-weight: 700; color: var(--ink); letter-spacing: 0.5px;
  }

  .holder { position: absolute; right: 32px; top: 232px; text-align: right; }
  .holder__name {
    font-size: 19px; font-weight: 700; color: var(--burgundy);
    text-transform: uppercase; letter-spacing: 0.3px;
  }
  .holder__rule {
    position: absolute; left: 32px; right: 32px; top: 262px;
    height: 2px; background: var(--ink);
  }
  .holder__title {
    position: absolute; right: 32px; top: 269px;
    font-size: 16px; color: var(--gold);
  }

  .contacts { position: absolute; left: 32px; top: 280px; list-style: none; }
  .contacts__item {
    display: flex; align-items: center; gap: 9px;
    height: 24px; font-size: 17px; color: var(--ink);
  }
  .contacts__icon { width: 16px; height: 14px; fill: var(--burgundy); flex: none; }

  .footer-band { position: absolute; left: 0; bottom: 0; width: 665px; height: 34px; }
  .footer-band__company {
    position: absolute; right: 32px; bottom: 6px;
    font-size: 17px; color: var(--paper);
  }

  .back-brand { position: absolute; left: 0; right: 0; top: 62px; text-align: center; }
  .back-brand__mark {
    display: block; width: 207px; height: 211px; margin: 0 auto 14px;
    border: 2px solid var(--paper); background: var(--burgundy-deep);
  }
  .back-brand__name {
    font-size: 40px; font-weight: 700; color: var(--paper); letter-spacing: 0.5px;
  }
</style>
</head>
<body>
  <section class="card card--front">
    <div class="brand">
      <span class="brand__mark"></span>
      <div class="brand__name">BROVENNA</div>
    </div>

    <div class="holder"><div class="holder__name">Marcus T. Hollenbrand</div></div>
    <div class="holder__rule"></div>
    <div class="holder__title">CEO</div>

    <ul class="contacts">
      <li class="contacts__item">
        <svg class="contacts__icon" viewBox="0 0 16 14"><path d="M1 4 C1 1 15 1 15 4 L12 5 L11 3 H5 L4 5 Z M4 6 H12 L14 13 H2 Z"/></svg>
        555-294-6172
      </li>
      <li class="contacts__item">
        <svg class="contacts__icon" viewBox="0 0 16 14"><path d="M1 2 H15 V12 H1 Z" /><path d="M1 2 L8 8 L15 2" fill="none" stroke="#fff" stroke-width="1.3"/></svg>
        mark@brovennatrading.example
      </li>
      <li class="contacts__item">
        <svg class="contacts__icon" viewBox="0 0 16 14"><circle cx="8" cy="7" r="6.5"/><path d="M2 7 H14 M8 0.5 V13.5" stroke="#fff" stroke-width="1.2"/></svg>
        www.brovennatrading.example
      </li>
    </ul>

    <svg class="footer-band" viewBox="0 0 665 34" preserveAspectRatio="none">
      <path d="M0 6 H300 C312 6 316 10 320 12 L320 13 C316 11 312 10 300 13 H0 Z" fill="var(--gold)"/>
      <path d="M0 19 H300 C318 19 318 2 340 2 H665 V34 H0 Z" fill="var(--burgundy)"/>
      <path d="M0 6 H298 C308 6 312 8 316 9 L320 12 C314 14 308 14 298 14 H0 Z" fill="var(--gold)"/>
    </svg>
    <div class="footer-band__company">Brovenna Trading / Shipping, LLC</div>
  </section>

  <section class="card card--back">
    <div class="back-brand">
      <span class="back-brand__mark"></span>
      <div class="back-brand__name">BROVENNA</div>
    </div>
  </section>
</body>
</html>
```